Glen Hartwick's Personal Guitar Bench - a multi-use workstation for you and your guitar

A guitar workstation/stand. A furniture grade device that serves as a workstation to repair, restring, refurbish, clean, maintain, and ultimately display your guitar. The guitar can be held held securely and safely lying on it back, it's face, either side, and comes with a stand for it to slide in when work is complete to display or Store.

Target Market(s)

Electric, acoustic, and most other guitar owners. Luthiers. Guitar techs.

Industry/Entity Type

Music Training

Requirements
Must have
• Needs to explain what the Workshop does, hit on the aesthetics, size, founder/inventor etc. I forwarded much verbiage that has been used from other sources with my pictures. Our website is glenhartwickbench.com which should be somewhere on the Brochure as well. Maybe bullet points. - for use with acoustic, electric, and most guitars - holds guitar face up, face down, either side, and a vertical display with stand. - made with non-reactive materials at guitar touch points - use for repairing refurbishing, cleaning, restringing, constructing, and maintaining - Any more you can think of. We are not 100% sure of the materials we are using yet so instead of being specific say something like made with only the highest grade materials, furniture-grade quality
Nice to have
• We are down-to-earth people wanting to show people a high-quality product. We are taking these brochures to TORVEX January2018. There will be over 100,000 music people/celebrities/buyers there. So we have one shot. Hoping you can help us with an awesome brochure. The colors on our website would be nice Glenhartwickbench.com
Should not have
• Cute

```html
<!DOCTYPE html>
<html lang="en">
<head>
<meta charset="utf-8">
<title>The Personal Guitar Bench – Brochure Outside</title>
<link href="https://fonts.googleapis.com/css2?family=Montserrat:wght@400;500;600;700;900&family=Kaushan+Script&display=swap" rel="stylesheet">
<style>
  :root{
    --bg:#e6e6e6;
    --paper:#ffffff;
    --ink:#2a2623;
    --copper:#c8874a;
    --gold:#c9a57a;
    --gold-light:#e2c7a0;
    --dark:#141210;
    --dark-2:#2a2522;
    --wood-1:#1e1410;
    --wood-2:#3a2418;
    --cream:#f4ecdf;
  }
  *{box-sizing:border-box;margin:0;padding:0}
  html,body{width:1200px;height:1001px;overflow:hidden}
  body{background:var(--bg);font-family:"Montserrat",sans-serif;color:var(--ink);position:relative}

  .brochure{position:absolute;left:45px;top:52px;width:1092px;height:858px;display:flex;box-shadow:0 10px 30px rgba(0,0,0,.25)}
  .panel{position:relative;width:364px;height:100%;overflow:hidden}
  .panel-bg{position:absolute;inset:0;width:100%;height:100%}
  .panel>*:not(.panel-bg){position:relative}

  /* Features panel */
  .features{background:var(--paper);padding:34px 22px 0 24px}
  .features-title{text-align:center;margin-bottom:22px}
  .features-title .kicker{display:block;font-size:19px;font-weight:400;color:var(--copper);letter-spacing:.5px}
  .features-title .main{display:block;font-size:22px;font-weight:700;color:var(--ink);margin-top:2px}
  .features-title .rule{display:block;width:150px;height:2px;margin:8px auto 0;background:linear-gradient(90deg,transparent,var(--gold),transparent)}
  .feature{margin-bottom:14px}
  .feature h3{font-size:15px;font-weight:600;color:var(--copper);margin-bottom:4px}
  .feature p{font-size:11.4px;line-height:1.36;color:#3a3633;text-align:justify}

  .stand-thumb{position:absolute!important;left:22px;top:668px;width:62px;height:150px;border-radius:30px 30px 6px 6px;background:linear-gradient(180deg,#e8783a,#3a2a24 70%)}
  .brand-mark{text-align:center;color:var(--cream)}
  .brand-mark .name{display:block;font-weight:500;letter-spacing:1px}
  .brand-mark .sub{display:block;font-weight:500;letter-spacing:1.2px;margin-top:4px}
  .features .brand-mark{position:absolute!important;left:110px;top:730px;width:220px}
  .features .brand-mark .name{font-size:18px}
  .features .brand-mark .sub{font-size:7px}
  .url{font-size:14px;letter-spacing:1.5px;color:var(--gold);font-weight:500}
  .features .url{position:absolute!important;left:100px;top:798px;width:240px;text-align:center}

  /* About panel */
  .about{background:linear-gradient(90deg,var(--wood-1),var(--wood-2) 35%,#2b1a12 60%,var(--wood-2) 85%,var(--wood-1));padding:38px 22px 0}
  .about-title{text-align:center}
  .about-title .kicker{display:block;font-size:25px;color:#fff;font-weight:400}
  .about-title .name{display:block;font-family:"Kaushan Script",cursive;font-size:36px;color:var(--gold-light);margin-top:-2px}
  .about p{font-size:12.8px;line-height:1.5;color:#f2ede6;text-align:justify;margin-top:18px}
  .about p+p{margin-top:14px}
  .about .brand-mark{margin-top:62px}
  .about .brand-mark .name{font-size:21px;color:var(--gold-light)}
  .about .brand-mark .sub{font-size:6.5px;color:var(--gold-light)}
  .portrait{position:absolute!important;left:73px;top:503px;width:218px;height:218px;border-radius:50%;background:radial-gradient(circle at 50% 40%,#6c7a58,#2f3b2a 60%,#1b2430);border:7px solid #cfcfcf;box-shadow:0 0 0 6px #5a3520}
  .follow{position:absolute!important;left:0;top:765px;width:100%;text-align:center}
  .follow h4{font-size:16px;font-weight:500;color:#fff}
  .follow h4::after{content:"";display:block;width:28px;height:1px;background:var(--gold);margin:6px auto 0}
  .socials{display:flex;justify-content:center;gap:10px;margin-top:10px;list-style:none}
  .socials li{display:flex;align-items:center;gap:4px;font-size:9px;color:var(--gold-light);font-weight:500}
  .socials li::before{content:"";width:10px;height:10px;border-radius:50%;background:var(--gold)}
  .about .url{display:block;margin-top:22px;color:#fff}

  /* Cover panel */
  .cover{background:var(--paper)}
  .cover-title{position:absolute!important;left:24px;top:395px;transform:rotate(-90deg);transform-origin:0 0;display:flex;flex-direction:column;width:370px}
  .cover-title .the{font-size:40px;font-weight:500;color:#3b3836;letter-spacing:3px;line-height:1}
  .cover-title .guitar{font-size:86px;font-weight:900;color:var(--copper);line-height:.9;letter-spacing:-1px}
  .cover-title .word{font-size:34px;font-weight:400;color:#2a2623;letter-spacing:10px;line-height:1.1}
  .cover-stand{position:absolute!important;left:210px;top:20px;width:160px;height:580px;border-radius:80px 0 0 60px;background:linear-gradient(90deg,#e07a36,#3b2c25 50%,#e07a36)}
  .cover .brand-mark{position:absolute!important;left:20px;top:700px;width:324px}
  .cover .brand-mark .name{font-size:32px;color:#fff}
  .cover .brand-mark .sub{font-size:10px;color:#fff;margin-top:8px}
  .cover .url{position:absolute!important;left:0;top:790px;width:100%;text-align:center}

  .caption{position:absolute;left:0;top:930px;width:100%;text-align:center;font-size:24px;color:#111;letter-spacing:.5px}
</style>
</head>
<body>
<main class="brochure">

  <section class="panel features">
    <svg class="panel-bg" viewBox="0 0 364 858" preserveAspectRatio="none" aria-hidden="true">
      <defs><linearGradient id="fade" x1="0" y1="0" x2="0" y2="1"><stop offset="0" stop-color="#fff"/><stop offset="1" stop-color="#f0f0f0"/></linearGradient></defs>
      <rect width="364" height="858" fill="url(#fade)"/>
      <path d="M0 640 Q180 700 364 650 L364 858 L0 858Z" fill="#c9a57a"/>
      <path d="M0 650 Q180 712 364 662 L364 830 L0 830Z" fill="#141210"/>
      <rect y="830" width="364" height="28" fill="#c9a57a"/>
    </svg>
    <h2 class="features-title"><span class="kicker">THE GUITAR</span><span class="main">BENCH FEATURES</span><span class="rule"></span></h2>
    <article class="feature"><h3>Uses</h3><p>How you use your Personal Guitar Bench (PGB) is a personal matter. But we'll give you some suggestions. You can use just one of them, all of them, or you just may think of your own. Restringing – repairing – cleaning – polishing – storing – holding – displaying</p></article>
    <article class="feature"><h3>Positioning and Design</h3><p>The PGB was designed for use with most guitars. It can be held firmly with the guitar lying on its front, on its back, or on its side. It comes with a cool sturdy stand that the PGB securely slides into for a vertical display or stand for your guitar.</p></article>
    <article class="feature"><h3>Materials</h3><p>Only high-quality materials are used in the construction of the PGB. A nonreactive Polymer is used on all parts that make contact with your guitar. Your guitar will be safe in its bench!</p></article>
    <article class="feature"><h3>Engineering</h3><p>The original bench that came from Glen's mind and hands was awesome. But Glen, being a perfectionist, thought that it could be better. So he sought out the five best engineers he could find 2500 miles away and let them go to work on it. The construction, soundness, and aesthetics are no longer awesome. They're phenomenal!</p></article>
    <article class="feature"><h3>Environment</h3><p>We care about the environment. And we love trees! For every one bench sold two trees will be planted. That's a promise!</p></article>
    <div class="stand-thumb" role="img" aria-label="Photo of the guitar bench in its display stand"></div>
    <div class="brand-mark"><span class="name">Glen Hartwick</span><span class="sub">PERSONAL GUITAR BENCH</span></div>
    <span class="url">www.glenhartwickbench.com</span>
  </section>

  <section class="panel about">
    <svg class="panel-bg" viewBox="0 0 364 858" preserveAspectRatio="none" aria-hidden="true">
      <rect width="364" height="6" fill="#c9a57a"/>
      <path d="M0 660 Q200 610 364 560 L364 858 L0 858Z" fill="#c9a57a"/>
      <path d="M0 670 Q200 622 364 572 L364 858 L0 858Z" fill="#141210"/>
      <rect y="808" width="364" height="50" fill="#3a3634"/>
    </svg>
    <h2 class="about-title"><span class="kicker">About</span><span class="name">Glen Hartwick</span></h2>
    <p>You will likely find Glen working in his wood shop in a small town in northern Idaho. He will be exploring ways to bring to life what he envisioned at last-night's campfire. He will be inspired by the sights and sounds of nature. In his mind's eye his vision will be something useful, something beautiful, and likely something you've never seen before.</p>
    <p>Glen loves music, all kinds. He loves guitars. Put together these passions with Glen's integrity and tenacious personality and you can bet there will come to life a product you would be happy to own and proud to give.</p>
    <div class="brand-mark"><span class="name">Glen Hartwick</span><span class="sub">PERSONAL GUITAR BENCH</span></div>
    <div class="portrait" role="img" aria-label="Portrait photo of founder Glen Hartwick outdoors"></div>
    <div class="follow">
      <h4>Follow Us</h4>
      <ul class="socials"><li>Chirper</li><li>Facepage</li><li>Vidstream</li><li>Pinboard</li></ul>
      <span class="url">www.glenhartwickbench.com</span>
    </div>
  </section>

  <section class="panel cover">
    <svg class="panel-bg" viewBox="0 0 364 858" preserveAspectRatio="none" aria-hidden="true">
      <defs><linearGradient id="mtn" x1="0" y1="0" x2="0" y2="1"><stop offset="0" stop-color="#ffffff"/><stop offset=".45" stop-color="#f2efeb"/><stop offset="1" stop-color="#b9b0a6"/></linearGradient></defs>
      <rect width="364" height="858" fill="url(#mtn)"/>
      <path d="M0 620 Q160 590 364 680 L364 858 L0 858Z" fill="#c9a57a"/>
      <path d="M0 632 Q160 604 364 694 L364 830 L0 830Z" fill="#141210"/>
      <rect y="830" width="364" height="28" fill="#c9a57a"/>
    </svg>
    <div class="cover-stand" role="img" aria-label="Photo of the guitar bench cradle with its wooden frame"></div>
    <h1 class="cover-title"><span class="the">THE PERSONAL</span><span class="guitar">GUITAR</span><span class="word">BENCH</span></h1>
    <div class="brand-mark"><span class="name">Glen Hartwick</span><span class="sub">PERSONAL GUITAR BENCH</span></div>
    <span class="url">www.glenhartwickbench.com</span>
  </section>

</main>
<p class="caption">BROCHURE_ OUTSIDE</p>
</body>
</html>
```